MARLOWE BRIGHT WORKS WEBSITE HOME PAGE AND CHECKOUT PAGES

UPDATE TO BRIEF:

Marlowe Bright Works is a company that provides Charities with the Free Vacation Vouchers that they can use to incentivize people to donate which in turn increases donations for the chairty.

So I need to keep it a little more template like the example url I gave. http://pagefernly.com/marlowe-bright-work/ Because, I am going to provide template to ANY CHARITY TYPE and they just fill in the content into the template and change images or whatever for their charity. So I am really looking for a website template that can be used for multiple and different kinds of charities.

So where the logo would go please use YOUR LOGO HERE generic logo for now

and where ever you promote the Free Vacation Certificate To Las Vegas please add "Brought To You By" (logo marlowe bright works or something...basically its a partnership with the Charity and Marlowe Bright Work)

So Marlowe Bright Work is a marketing company and not a Charity but more of a plug and play platform that allows a charity to accepts donations and immediately deliver the promised incentive offer after donation is made on the website.

When a Charity is able to offer a high perceived value gift for a donation they increase donations.

Target Market(s)

PEOPLE THAT DONATE TO CHARITIES

Industry/Entity Type

Charity

Number of Pages Required

3 page

Requirements
Must have
• One thing i need to add to the website is an Incentive Gift for the Donation.

So I need this tagline and images to make the promotion seem great:
"Donate $100 and Receive A Free 3 Night Vacation Certificate To Las Vegas!"

Maybe show image of vegas or some kind of nice graphic that promotes the vegas vacation as a gift for the $100 donation very well"

I need the payment pages as well. So when someone click Donate Now, the next page is there where they can see their gift that is included with the donation, and also the donation amount...
Nice to have

Should not have

```html
<!DOCTYPE html>
<html lang="en">
<head>
<meta charset="utf-8">
<title>Marlowe Bright Works – Home</title>
<link rel="stylesheet" href="https://fonts.googleapis.com/css2?family=Noto+Sans:wght@400;700;800&family=Nunito+Sans:wght@300;400&display=swap">
<style>
  :root{
    --orange:#ff7c00;
    --ink:#1d1d1d;
    --nav-text:#555555;
    --body-warm:#9a8777;
    --body-grey:#7a7a7a;
    --mist:#f3f3f3;
    --white:#ffffff;
    --night:#0f1b26;
  }
  *{box-sizing:border-box;margin:0;padding:0}
  html,body{width:1200px;height:3045px;overflow:hidden;background:var(--white)}
  body{font-family:"Noto Sans",Arial,sans-serif;color:var(--ink)}
  .page{position:relative;width:1200px;height:3045px;overflow:hidden}

  /* navigation */
  .site-nav{position:absolute;top:0;left:0;width:1200px;height:76px;background:var(--white)}
  .site-nav a{position:absolute;top:39px;font-size:15px;color:var(--nav-text);text-decoration:none}
  .site-nav a.is-active{color:var(--orange)}
  .brand{position:absolute;display:flex;align-items:center;gap:9px;font-weight:700;color:var(--nav-text);white-space:nowrap}
  .brand-square{width:30px;height:30px;background:var(--orange);flex:none}
  .brand-header{left:494px;top:18px;font-size:20px;line-height:20px}
  .brand-footer{left:462px;top:2772px;font-size:26px;line-height:26px}

  /* hero */
  .hero{position:absolute;top:76px;left:0;width:1200px;height:534px;
    background:radial-gradient(ellipse at 50% 55%,#4a3a33 0%,#2a2421 40%,#121212 75%,#0a0a0a 100%)}
  .hero-title{position:absolute;top:98px;width:100%;text-align:center;color:var(--white);font-weight:400}
  .hero-title strong{display:block;font-size:37px;font-weight:800;line-height:46px}
  .hero-title span{display:block;font-size:35px;font-weight:400;line-height:44px}
  .hero-cta{position:absolute;top:212px;left:509px;color:var(--white);font-size:23px;display:flex;align-items:center;gap:14px}
  .hero-cta u{text-underline-offset:4px}
  .hero-dots{position:absolute;top:514px;left:587px;display:flex;gap:6px}
  .hero-dots i{width:6px;height:6px;background:#cfcfcf;display:block}
  .hero-dots i:first-child{background:var(--white)}

  /* why care */
  .care-bg{position:absolute;top:610px;left:0}
  .section-title{font-size:23px;font-weight:700;color:var(--orange)}
  .care-title{position:absolute;top:693px;width:100%;text-align:center}
  .care-copy{position:absolute;left:196px;width:800px;text-align:center;font-family:"Nunito Sans",Arial,sans-serif;font-size:14.5px;line-height:22px;color:var(--body-warm)}
  .emblem{position:absolute;top:1040px;left:555px;width:90px;height:90px;border-radius:50%;background:var(--orange)}

  /* help */
  .help-title{position:absolute;left:151px;top:1144px}
  .help-copy{position:absolute;left:152px;width:610px;font-family:"Nunito Sans",Arial,sans-serif;font-size:14.5px;line-height:17px;color:var(--body-grey)}
  .help-photo{position:absolute;left:842px;top:1170px;width:188px;height:125px;
    background:linear-gradient(135deg,#cfcac2,#8b7c6e 55%,#e6e1d9)}
  .want-to{position:absolute;left:842px;top:1305px;width:188px;text-align:center;font-size:31px;line-height:40px;color:var(--ink)}
  .donate-box{position:absolute;left:841px;top:1348px;width:189px;height:47px;background:var(--orange);
    color:var(--white);font-weight:700;font-size:36px;text-align:center;line-height:46px;text-decoration:underline;text-underline-offset:4px}

  /* offer band */
  .offer-band{position:absolute;top:1481px;left:0;width:1200px;height:205px;background:var(--orange)}
  .offer-icon{position:absolute;left:142px;top:0;width:273px;height:205px;background:var(--white)}
  .offer-icon div{position:absolute;left:52px;top:22px;width:180px;height:162px;background:#ececec}
  .offer-text{position:absolute;left:454px;top:50px;color:var(--white);font-size:29px;line-height:36px}
  .offer-text b{font-weight:700}

  /* vegas */
  .vegas{position:absolute;top:1686px;left:0}
  .gift-title{position:absolute;top:1803px;left:374px;width:451px;text-align:center;font-weight:700}
  .gift-title .l1{color:var(--orange);font-size:52px;line-height:64px}
  .gift-title .l1 span{font-weight:400}
  .gift-title .l2{color:var(--white);font-size:54px;line-height:64px}
  .gift-title .l3{color:var(--orange);font-size:56px;line-height:66px}
  .vegas-cta{position:absolute;top:2345px;left:444px;width:312px;text-align:center;color:var(--white)}
  .vegas-cta u{display:block;font-size:42px;font-weight:700;line-height:52px;background:rgba(10,20,30,.55);text-underline-offset:5px}

  /* footer */
  .site-footer{position:absolute;top:2841px;left:0;width:1200px;height:204px;background:var(--orange);color:var(--white)}
  .footer-title{position:absolute;left:131px;top:40px;font-size:25px;font-weight:700}
  .email-field{position:absolute;left:131px;top:97px;width:250px;height:44px;background:var(--white);
    color:#666;font-size:13px;padding:13px 0 0 28px}
  .subscribe{position:absolute;left:393px;top:97px;width:103px;height:44px;border:2px solid var(--white);
    font-size:14px;text-align:center;line-height:40px}
  .social{position:absolute;top:118px;left:964px;display:flex;gap:26px}
  .social span{width:24px;height:24px;border-radius:50%;background:var(--ink);display:block}
  .copyright{position:absolute;right:104px;top:160px;font-size:14px;color:var(--ink)}
</style>
</head>
<body>
<div class="page">

  <nav class="site-nav">
    <a style="left:89px" href="#">Who we are</a>
    <a style="left:253px" class="is-active" href="#">About</a>
    <a style="left:375px" href="#">Causes</a>
    <div class="brand brand-header"><span class="brand-square"></span><span>Marlowe Bright<br>Works</span></div>
    <a style="left:789px" href="#">Stories</a>
    <a style="left:919px" href="#">Event</a>
    <a style="left:1039px" href="#">Contact</a>
  </nav>

  <section class="hero" role="img" aria-label="Photo of open cupped hands reaching out in the dark">
    <h1 class="hero-title"><strong>YOU CAN HELP</strong><span>TO SAVE THE WORLD</span></h1>
    <div class="hero-cta"><u>Donate Now</u>
      <svg width="40" height="20" viewBox="0 0 40 20"><path d="M1 10H38M29 2l9 8-9 8" fill="none" stroke="#fff" stroke-width="2"/></svg>
    </div>
    <div class="hero-dots"><i></i><i></i><i></i><i></i></div>
  </section>

  <svg class="care-bg" width="1200" height="480" viewBox="0 610 1200 480">
    <path d="M0 610H1200C1200 874 931 1088 600 1088C269 1088 0 874 0 610Z" fill="#f3f3f3"/>
  </svg>
  <h2 class="section-title care-title">WHY SHOULD I CARE</h2>
  <p class="care-copy" style="top:747px">Absolute poverty is the complete lack of the means necessary to meet basic personal needs, such as food, clothing and shelter.[2] The threshold at which absolute poverty is defined is always about the same, independent of the person's permanent location or era.</p>
  <p class="care-copy" style="top:835px">On the other hand, relative poverty occurs when a person cannot meet a minimum level of living standards, compared to others in the same time and place. Therefore, the threshold at which relative poverty is defined varies from one country to another, or from one society to another.[3] For example, a person who cannot afford housing better than a small tent in an open field would be said to live in relative poverty if almost everyone else in that area lives in modern brick homes, but not if everyone else also lives in small tents in open fields (for example, in a nomadic tribe).</p>
  <div class="emblem"></div>

  <h2 class="section-title help-title">HOW CAN YOU HELP</h2>
  <p class="help-copy" style="top:1203px">We want to do more and you can help. By committing a small fraction of your income to protect children in need, you can help save a child and contribute to humanity. You can donate as low as INR 500 per month.</p>
  <p class="help-copy" style="top:1270px">While Brightpath Kids Fund appreciates monthly donations where you choose to donate a small fixed amount monthly for us to be able to plan our programmes for a longer term, a single donation can also help save a child.</p>
  <p class="help-copy" style="top:1338px">You will get your tax exemption certificate within 15 days of your one-time donation (quarterly in case of regular donors, who pledge monthly donations, after their first month’s donation). You will get quarterly updates on how you are making a difference.</p>
  <div class="help-photo" role="img" aria-label="Photo of many hands joined together in a circle"></div>
  <div class="want-to">I WANT TO</div>
  <div class="donate-box">DONATE</div>

  <section class="offer-band">
    <div class="offer-icon"><div role="img" aria-label="Illustration of a heart resting on an open hand"></div></div>
    <p class="offer-text"><b>"Donate $100</b> &amp;<br>Receive A Free 3 Night<br><b>Vacation Certificate To Las Vegas!"</b></p>
  </section>

  <svg class="vegas" width="1200" height="1012" viewBox="0 1686 1200 1012" role="img" aria-label="Night aerial photo of the Las Vegas strip with lit hotels and a fountain lake">
    <defs>
      <linearGradient id="vegasSky" x1="0" y1="0" x2="0" y2="1">
        <stop offset="0" stop-color="#2f6aa8"/>
        <stop offset=".3" stop-color="#5b6f86"/>
        <stop offset=".45" stop-color="#a07a4a"/>
        <stop offset=".65" stop-color="#1f3a55"/>
        <stop offset="1" stop-color="#3a2a1e"/>
      </linearGradient>
    </defs>
    <path d="M0 1686H1200V2140C1150 2480 900 2698 600 2698C300 2698 50 2480 0 2140Z" fill="url(#vegasSky)"/>
    <path d="M374 1686H825V1840C825 1965 724 2069 600 2069C476 2069 374 1965 374 1840Z" fill="#0f1b26" opacity=".92"/>
  </svg>
  <div class="gift-title">
    <div class="l1">Gift <span>for the</span></div>
    <div class="l2">$100</div>
    <div class="l3">Donation</div>
  </div>
  <div class="vegas-cta"><u>Donate Now</u>
    <svg width="66" height="30" viewBox="0 0 66 30" style="margin-top:8px"><path d="M1 15H64M50 2l14 13-14 13" fill="none" stroke="#fff" stroke-width="2.5"/></svg>
  </div>

  <div class="brand brand-footer"><span class="brand-square" style="width:38px;height:38px"></span><span>Marlowe Bright<br>Works</span></div>

  <footer class="site-footer">
    <h3 class="footer-title">Get updates on what we're doing</h3>
    <div class="email-field">E - mail address</div>
    <div class="subscribe">SUBSCRIBE</div>
    <div class="social" aria-label="Social links"><span></span><span></span><span></span></div>
    <p class="copyright">© 2020 Marlowe Bright Work. All rights reserved.</p>
  </footer>

</div>
</body>
</html>
```